New Zealand Marlborough Sauvignon Blanc wine packaging design

We need packaging design for our new wine brand, Dunmore Hale. The wine is a New Zealand Marlborough Sauvignon Blanc. We would like the packaging will portray elegance and style with an understated label. We are looking for a label that portrays the elegance of the French Riviera. The label should be round or pill shaped.
Updates

Industry/Entity Type

Wine

Font styles to use
Serif
Sans Serif

Requirements
Must have
• The words in order of importance: Dunmore Hale, Sauvignon Blanc, Marlborough, New Zealand. It should be fit to the bottle posted in the links
Nice to have
• a pill shape or circular shape
Should not have
• Illustrations of wine bottles, wine glasses, or grapes

```html
<!DOCTYPE html>
<html lang="en">
<head>
<meta charset="utf-8">
<title>Dunmore Hale Sauvignon Blanc – Label</title>
<link rel="stylesheet" href="https://fonts.googleapis.com/css2?family=Libre+Caslon+Text:wght@400;700&family=Pinyon+Script&display=swap">
<style>
  :root {
    --paper: #ffffff;
    --ink: #111111;
    --ornament-tone: #e2e2e2;
  }
  html, body {
    margin: 0;
    padding: 0;
    width: 1200px;
    height: 900px;
    overflow: hidden;
    background: var(--paper);
  }
  .label {
    display: block;
    width: 1200px;
    height: 900px;
  }
  .label-edge {
    fill: var(--paper);
    stroke: var(--ink);
    stroke-width: 1.2;
  }
  .brand-name {
    font-family: "Libre Caslon Text", Georgia, serif;
    font-weight: 400;
    font-size: 78px;
    fill: var(--ink);
  }
  .varietal {
    font-family: "Pinyon Script", cursive;
    font-size: 74px;
    fill: var(--ink);
  }
  .region {
    font-family: "Libre Caslon Text", Georgia, serif;
    font-weight: 700;
    font-size: 40px;
    fill: var(--ink);
  }
  .country {
    font-family: "Libre Caslon Text", Georgia, serif;
    font-weight: 700;
    font-size: 26px;
    fill: var(--ink);
  }
  .ornament-area {
    fill: var(--ornament-tone);
  }
</style>
</head>
<body>
<svg class="label" viewBox="0 0 1200 900" xmlns="http://www.w3.org/2000/svg">
  <defs>
    <path id="brand-arc" d="M 397 458 A 203 313 0 0 1 803 458"/>
  </defs>

  <ellipse class="label-edge" cx="600" cy="450" rx="295" ry="418"/>

  <text class="brand-name" text-anchor="middle">
    <textPath href="#brand-arc" startOffset="50%" textLength="780" lengthAdjust="spacing">DUNMORE HALE</textPath>
  </text>

  <path class="ornament-area" d="M 456 290 L 456 268 Q 482 176 600 172 Q 718 176 744 268 L 744 290 Z"
        role="img" aria-label="Ornamental arched scroll with trailing leaves"/>

  <g role="img" aria-label="Ornamental flourish divider with scrolls">
    <rect class="ornament-area" x="526" y="440" width="148" height="46" rx="14"/>
    <rect class="ornament-area" x="412" y="484" width="376" height="34" rx="17"/>
  </g>

  <text class="varietal" x="600" y="597" text-anchor="middle" textLength="428" lengthAdjust="spacingAndGlyphs">Sauvignon Blanc</text>

  <rect class="ornament-area" x="473" y="640" width="259" height="14" rx="7"
        role="img" aria-label="Small leafy vine divider"/>

  <text class="region" x="602" y="732" text-anchor="middle" textLength="259" lengthAdjust="spacing">Marlborough</text>
  <text class="country" x="629" y="772" text-anchor="middle" textLength="176" lengthAdjust="spacing">New Zealand</text>
</svg>
</body>
</html>
```